Business Card Design - Law Firm

We are a boutique law firm located near the beach in Manly, Australia. We have recently had a new logo designed and are revamping our business cards with the new logo.

We have recently had a business card design done for us but are not entirely happy with it. We are looking for something modern, simplistic but striking. We would like to see multiple designs.

We have attached a word document which includes our new logo and the current business card design which we are looking at moving away from.

We would like the business cards to be double sided. We would like the design to include something which we can print in gloss colour when we send it to the business card printers.

```html
<!DOCTYPE html>
<html lang="en">
<head>
<meta charset="utf-8">
<title>Harbourne &amp; Associates – Business Cards</title>
<link rel="stylesheet" href="https://fonts.googleapis.com/css2?family=Montserrat:wght@500;700;800&family=Roboto:wght@400&display=swap">
<style>
  :root {
    --backdrop: #3b3b3d;
    --card: #ffffff;
    --navy: #34479a;
    --gold: #b9a46a;
    --ink: #2a2a2a;
    --text: #4a4a4a;
  }
  * { box-sizing: border-box; margin: 0; padding: 0; }
  html, body { width: 1200px; height: 905px; overflow: hidden; }
  body {
    background: var(--backdrop);
    position: relative;
    font-family: "Roboto", Arial, sans-serif;
  }
  .card {
    position: absolute;
    left: 310px;
    width: 580px;
    height: 332px;
    background: var(--card);
    border-radius: 16px;
    overflow: hidden;
    box-shadow: 0 10px 28px rgba(0,0,0,.45);
  }
  .card--front { top: 90px; }
  .card--back  { top: 482px; }

  .brand {
    display: flex;
    align-items: center;
    gap: 10px;
    font-family: "Montserrat", Arial, sans-serif;
    font-weight: 700;
    color: var(--ink);
    letter-spacing: .5px;
  }
  .brand__dot {
    border-radius: 50%;
    background: var(--navy);
    flex: none;
  }
  .card--front .brand {
    position: absolute;
    top: 50%; left: 50%;
    transform: translate(-50%, -50%);
    font-size: 24px;
    white-space: nowrap;
  }
  .card--front .brand__dot { width: 26px; height: 26px; }

  .card--back .brand {
    position: absolute;
    top: 40px; left: 38px;
    font-size: 17px;
  }
  .card--back .brand__dot { width: 18px; height: 18px; }

  .holder {
    position: absolute;
    top: 34px; right: 40px;
    text-align: right;
  }
  .holder__name {
    font-family: "Montserrat", Arial, sans-serif;
    font-weight: 800;
    font-size: 27px;
    color: var(--navy);
    letter-spacing: .3px;
  }
  .holder__name .surname { color: var(--gold); }
  .holder__role {
    font-size: 14px;
    color: var(--text);
    margin-top: 2px;
  }
  .divider {
    position: absolute;
    left: 40px; right: 40px;
    top: 118px;
    height: 1.5px;
    background: var(--gold);
  }
  .contact {
    position: absolute;
    left: 40px;
    bottom: 48px;
    list-style: none;
    font-size: 14.5px;
    color: var(--text);
  }
  .contact li {
    display: flex;
    align-items: center;
    gap: 9px;
    line-height: 25px;
  }
  .contact svg { width: 13px; height: 13px; fill: var(--navy); flex: none; }
  .address {
    position: absolute;
    right: 40px;
    bottom: 60px;
    font-style: normal;
    font-size: 14.5px;
    line-height: 20px;
    color: var(--text);
    text-align: right;
  }
  .band {
    position: absolute;
    left: 0; right: 0; bottom: 0;
    height: 16px;
    background: var(--navy);
  }
</style>
</head>
<body>
  <section class="card card--front" aria-label="Card front">
    <div class="brand"><span class="brand__dot"></span>Harbourne &amp; Associates</div>
  </section>

  <section class="card card--back" aria-label="Card back">
    <div class="brand"><span class="brand__dot"></span>Harbourne &amp; Associates</div>

    <div class="holder">
      <div class="holder__name">Nadia <span class="surname">Whitlock</span></div>
      <div class="holder__role">Practice Manager</div>
    </div>

    <div class="divider"></div>

    <ul class="contact">
      <li>
        <svg viewBox="0 0 24 24" aria-hidden="true"><path d="M6.6 10.8a15.1 15.1 0 0 0 6.6 6.6l2.2-2.2c.3-.3.7-.4 1-.2 1.1.4 2.3.6 3.6.6.6 0 1 .4 1 1V20c0 .6-.4 1-1 1A17 17 0 0 1 3 4c0-.6.4-1 1-1h3.5c.6 0 1 .4 1 1 0 1.3.2 2.5.6 3.6.1.3 0 .7-.2 1l-2.3 2.2z"/></svg>
        (02) 9000 4187
      </li>
      <li>
        <svg viewBox="0 0 24 24" aria-hidden="true"><path d="M2 5h20v14H2V5zm2 2v.5l8 5 8-5V7H4zm0 2.8V17h16V9.8l-8 5-8-5z"/></svg>
        nadia.whitlock@coastlaw.com.au
      </li>
      <li>
        <svg viewBox="0 0 24 24" aria-hidden="true"><path d="M12 2a10 10 0 1 0 0 20 10 10 0 0 0 0-20zm6.9 6h-3a15.7 15.7 0 0 0-1.3-3.9A8 8 0 0 1 18.9 8zM12 4c.8 1.2 1.5 2.5 1.9 4h-3.8c.4-1.5 1.1-2.8 1.9-4zM4.3 14a8 8 0 0 1 0-4h3.4a16 16 0 0 0 0 4H4.3zm.8 2h3a15.7 15.7 0 0 0 1.3 3.9A8 8 0 0 1 5.1 16zm3-8h-3a8 8 0 0 1 4.3-3.9C8.8 5.3 8.4 6.6 8.1 8zM12 20c-.8-1.2-1.5-2.5-1.9-4h3.8c-.4 1.5-1.1 2.8-1.9 4zm2.3-6H9.7a14.6 14.6 0 0 1 0-4h4.6a14.6 14.6 0 0 1 0 4zm.3 5.9c.6-1.2 1-2.5 1.3-3.9h3a8 8 0 0 1-4.3 3.9zm1.7-5.9a16 16 0 0 0 0-4h3.4a8 8 0 0 1 0 4h-3.4z"/></svg>
        www.harbourneassociates.com.au
      </li>
    </ul>

    <address class="address">Suite 4, 12 Tidewater Lane<br>BAYVIEW NSW 2104</address>

    <div class="band"></div>
  </section>
</body>
</html>
```